Independent Statistical Consultant Business Card

I will be going out as an independent statistical consultant and need a business card. I specialize in data analysis and statistics for health care and public health

I am an Licensed Numeric Examiner from the Coastal Metrics Society. Would like to incorporate that logo into the design

The design should be modern with classic colors, convey accuracy, analytic creativity and responsiveness to client needs.

The name of the firm will be simply Tim Halvarsen Numeric Insight Services

To all designers, I want to clarify that the DCred logo and the phrase Licensed Numeric Examiner are not the name of the company nor the focus of the card. They are equivalent to being a Veltrano Qualified Engineer (VQE) but in the area of statistics The name of the firm will be: Tim Halvarsen, Numeric Insight Services. I look forward to your submissions. Thanks. Tim

```html
<!DOCTYPE html>
<html lang="en">
<head>
<meta charset="utf-8">
<title>Tim Halvarsen — Numeric Insight Services</title>
<link rel="stylesheet" href="https://fonts.googleapis.com/css2?family=Ubuntu:wght@400;500;700&display=swap">
<style>
  :root {
    --backdrop: #e9e6e1;
    --card: #ffffff;
    --ink: #1b1b1b;
    --navy: #0b2e63;
    --band-blue: #1a5fab;
    --base-blue: #7fb0de;
    --curve-red: #f3a68f;
    --curve-green: #92d6b0;
    --curve-yellow: #f5efa8;
    --curve-purple: #a9a1d2;
  }
  * { margin: 0; padding: 0; box-sizing: border-box; }
  html, body {
    width: 1200px; height: 1000px; overflow: hidden;
    background: var(--backdrop);
    font-family: "Ubuntu", sans-serif;
  }
  .business-card {
    position: absolute; left: 100px; top: 215px;
    width: 1000px; height: 570px;
    background: var(--card);
    overflow: hidden;
    box-shadow: 0 6px 24px rgba(0,0,0,0.18);
  }
  .holder-name {
    position: absolute; left: 77px; top: 50px;
    font-size: 64px; font-weight: 400; color: var(--ink);
    letter-spacing: 1px; line-height: 1;
  }
  .name-rule {
    position: absolute; left: 77px; top: 119px;
    width: 629px; height: 3px; background: var(--navy);
  }
  .firm-name {
    position: absolute; left: 77px; top: 128px;
    font-size: 37px; font-weight: 400; color: var(--ink);
    line-height: 1;
  }
  .credential {
    position: absolute; left: 706px; top: 64px;
    width: 229px; height: 109px;
    display: flex; align-items: center; justify-content: center; gap: 12px;
  }
  .credential-mark {
    width: 22px; height: 22px; background: var(--navy);
  }
  .credential-name {
    font-size: 46px; font-weight: 400; color: var(--navy); line-height: 1;
  }
  .pattern-band {
    position: absolute; left: 0; top: 232px;
    width: 100%; height: 112px;
    background: var(--band-blue);
  }
  .contact {
    position: absolute; left: 77px; top: 423px;
    font-size: 27px; color: var(--ink); line-height: 40px;
  }
  .contact-label { font-weight: 700; }
  .distribution-art {
    position: absolute; left: 572px; top: 350px;
    width: 329px; height: 180px;
    background: linear-gradient(90deg, var(--curve-purple) 0%, var(--curve-red) 30%, var(--curve-yellow) 50%, var(--curve-green) 62%, var(--curve-purple) 100%);
    opacity: 0.6;
  }
  .base-strip {
    position: absolute; left: 0; top: 0;
  }
</style>
</head>
<body>
  <main class="business-card">
    <div class="holder-name">Tim Halvarsen</div>
    <div class="name-rule"></div>
    <div class="firm-name">Numeric Insight Services</div>

    <div class="credential" aria-label="DCred — Licensed Numeric Examiner">
      <span class="credential-mark"></span>
      <span class="credential-name">DCred</span>
    </div>

    <div class="pattern-band" role="img" aria-label="Blue band with scattered translucent squares"></div>

    <div class="contact">
      <p><span class="contact-label">phone:</span> 555 014 2287</p>
      <p><span class="contact-label">email:</span> tim@halvarsenstats.com</p>
    </div>

    <div class="distribution-art" role="img" aria-label="Overlapping coloured distribution curves illustration"></div>

    <svg class="base-strip" width="1000" height="570" viewBox="0 0 1000 570" aria-hidden="true">
      <path d="M74,549 L928,549 L948,570 L56,570Z" fill="var(--base-blue)"/>
    </svg>
  </main>
</body>
</html>
```